Varrow Property Group Business cards

I am starting a property development and consultancy business called Varrow Property Group. I have a logo designed and a website on its way:
www.varrowgroup-example.com.au

I need a business card with the following:

Front:
Mostly orange with logo taking up all front of card

Back of card:
Logo

Miles Harcourt
Managing Director

T +61 455 207 364
E miles.harcourt@varrowgroup-example.com.au
www.varrowgroup-example.com.au

Industry/Entity Type

Business

Requirements
Must have
• curved edges

```html
<!DOCTYPE html>
<html lang="en">
<head>
<meta charset="utf-8">
<title>Varrow Property Group — Business Card</title>
<link rel="stylesheet" href="https://fonts.googleapis.com/css2?family=Ubuntu+Condensed&family=Michroma&family=Jura:wght@300;400&family=Cabin+Condensed:wght@400&display=swap">
<style>
  :root {
    --orange: #f9ac1f;
    --ink: #3b3b3b;
    --paper: #ffffff;
    --guide: #e2e2e2;
    --label: #1a1a1a;
  }
  html, body {
    margin: 0;
    padding: 0;
    width: 1200px;
    height: 900px;
    overflow: hidden;
    background: var(--paper);
  }
  .sheet { display: block; width: 1200px; height: 900px; }

  .guide-line { stroke: var(--guide); stroke-width: 1; }
  .dimension-label {
    font-family: "Cabin Condensed", "Arial Narrow", sans-serif;
    font-weight: 400;
    font-size: 20px;
    fill: var(--label);
  }
  .dimension-label .small-cap { font-size: 15px; }
  .side-label {
    font-family: "Ubuntu Condensed", "Arial Narrow", sans-serif;
    font-size: 80px;
    fill: var(--orange);
  }
  .side-label--back { font-size: 67px; }

  .card-edge { fill: none; stroke: var(--orange); stroke-width: 4; }
  .brand-band { fill: var(--orange); }
  .divider { stroke: var(--orange); stroke-width: 3; }

  .brand-name {
    font-family: "Ubuntu Condensed", "Arial Narrow", sans-serif;
    fill: var(--paper);
  }
  .brand-name--front { font-size: 156px; }
  .brand-name--back { font-size: 68px; }

  .brand-tagline {
    font-family: "Michroma", sans-serif;
    fill: var(--ink);
  }
  .brand-tagline--front { font-size: 27px; }
  .brand-tagline--back { font-size: 11px; }

  .holder-name {
    font-family: "Ubuntu Condensed", "Arial Narrow", sans-serif;
    font-size: 78px;
    fill: var(--orange);
  }
  .holder-name .small-cap { font-size: 62px; }
  .holder-role {
    font-family: "Jura", sans-serif;
    font-weight: 300;
    font-size: 25px;
    fill: var(--ink);
  }
  .website {
    font-family: "Jura", sans-serif;
    font-weight: 300;
    font-size: 21px;
    fill: var(--ink);
  }
  .phone {
    font-family: "Michroma", sans-serif;
    font-size: 22px;
    fill: var(--ink);
  }
  .email {
    font-family: "Jura", sans-serif;
    font-weight: 400;
    font-size: 12px;
    fill: var(--ink);
  }
</style>
</head>
<body>
<svg class="sheet" viewBox="0 0 1200 900" xmlns="http://www.w3.org/2000/svg">

  <!-- Dimension guides -->
  <g class="dimensions">
    <line class="guide-line" x1="193" y1="65.5" x2="967" y2="65.5"/>
    <text class="dimension-label" x="517" y="62" textLength="68" lengthAdjust="spacingAndGlyphs">3,5 I<tspan class="small-cap">NCH</tspan></text>
    <line class="guide-line" x1="1003.5" y1="103" x2="1003.5" y2="569"/>
    <text class="dimension-label" x="1011" y="317" textLength="44" lengthAdjust="spacingAndGlyphs">2 I<tspan class="small-cap">NCH</tspan></text>
  </g>

  <!-- Front of card -->
  <g class="card card--front">
    <rect class="card-edge" x="195" y="103" width="770" height="465" rx="22" ry="22"/>
    <rect class="brand-band" x="397" y="192" width="571" height="138"/>
    <line class="divider" x1="399.5" y1="192" x2="399.5" y2="570"/>

    <text class="website" x="468" y="152" textLength="468" lengthAdjust="spacing">www.varrowgroup-example.com.au</text>

    <text class="brand-name brand-name--front" x="470" y="330" textLength="468" lengthAdjust="spacingAndGlyphs">VARROW</text>
    <text class="brand-tagline brand-tagline--front" x="575" y="376" textLength="360" lengthAdjust="spacingAndGlyphs">PROPERTY GROUP</text>

    <text class="phone" x="666" y="443" textLength="269" lengthAdjust="spacingAndGlyphs">+61 455 207 364</text>
    <text class="email" x="655" y="464" textLength="279" lengthAdjust="spacingAndGlyphs">miles.harcourt@varrowgroup-example.com.au</text>

    <text class="holder-name" transform="translate(316 533) rotate(-90)" textLength="395" lengthAdjust="spacingAndGlyphs">M<tspan class="small-cap">ILES</tspan> H<tspan class="small-cap">ARCOURT</tspan></text>
    <text class="holder-role" transform="translate(344 418) rotate(-90)" textLength="281" lengthAdjust="spacingAndGlyphs">Managing Director</text>
  </g>

  <text class="side-label" x="193" y="654" textLength="193" lengthAdjust="spacingAndGlyphs">FRONT</text>

  <!-- Back of card -->
  <g class="card card--back">
    <rect class="card-edge" x="636" y="608" width="329" height="198" rx="10" ry="10"/>
    <rect class="brand-band" x="633" y="627" width="188" height="59"/>
    <text class="brand-name brand-name--back" x="653" y="686" textLength="160" lengthAdjust="spacingAndGlyphs">VARROW</text>
    <text class="brand-tagline brand-tagline--back" x="656" y="705" textLength="160" lengthAdjust="spacingAndGlyphs">PROPERTY GROUP</text>
  </g>

  <text class="side-label side-label--back" transform="translate(1021 808) rotate(-90)" textLength="136" lengthAdjust="spacingAndGlyphs">BACK</text>
</svg>
</body>
</html>
```